Postcard design to acquire new clients for my Property Management Company

I'm looking for a postcard design that I can send to prospective clients detailing information about my company and services.
Postcard should be eye catching and contain information from www.brightkeyrentals-example.com. I've provided a few screen shots for the most important information and my logo.
Target Market(s)
Real Estate
Industry/Entity Type
Real Estate
Font styles to use
Sans Serif
Requirements
Must have
- Must be eye catching!! this will be a direct mail piece - I'd like for the card to be read and not tossed in the trash immediately.
Design que from the logo.
A place to write / print the receipts name and address.
our physical address - 2287 Marble Lane, Lubbock, TX 79555.
Should not have
- the contact information on the business card is not accurate - please use info from website.

```html
<!DOCTYPE html>
<html lang="en">
<head>
<meta charset="utf-8">
<title>BrightKey Property Management – Postcard</title>
<link href="https://fonts.googleapis.com/css2?family=Fira+Sans:ital,wght@0,300;0,400;0,600;1,400&family=Fira+Sans+Condensed:wght@400;500;600&display=swap" rel="stylesheet">
<style>
  :root{
    --stage:#d3d4d7;
    --navy:#14507e;
    --yellow:#f2e53a;
    --white:#ffffff;
    --overlay-a:#6f82b0;
    --overlay-b:#4f6596;
    --pink:#e0407a;
    --label:#f4f4f6;
  }
  *{box-sizing:border-box;margin:0;padding:0}
  html,body{width:1200px;height:823px;overflow:hidden;background:var(--stage)}
  body{position:relative;font-family:"Fira Sans",Arial,sans-serif}

  .card{position:absolute;top:220px;width:480px;height:339px;overflow:hidden}
  .card--front{left:108px}
  .card--back{left:614px;background:var(--white)}

  /* front */
  .front-photo{position:absolute;inset:0;background:linear-gradient(135deg,var(--overlay-a) 0%,#8093bd 45%,var(--overlay-b) 100%)}
  .front-copy{position:absolute;left:68px;top:118px;font-family:"Fira Sans Condensed",sans-serif}
  .headline{color:var(--yellow);font-weight:400;font-size:40px;line-height:40px;letter-spacing:.3px}
  .subhead{color:var(--yellow);font-weight:400;font-size:22px;line-height:24px;letter-spacing:1px;margin-top:2px}
  .tagline{color:var(--white);font-style:italic;font-size:13px;margin-top:6px;font-family:"Fira Sans",sans-serif}

  .brand{position:absolute;text-align:center;color:var(--white);font-family:"Fira Sans",sans-serif;font-weight:600}
  .brand__name{display:block;letter-spacing:5px}
  .brand__sub{display:block;letter-spacing:3.2px}
  .card--front .brand{left:0;right:0;top:246px}
  .card--front .brand__name{font-size:22px;line-height:24px}
  .card--front .brand__sub{font-size:10px;line-height:12px}

  .contact-row{position:absolute;left:38px;right:28px;top:301px;display:flex;justify-content:space-between;color:var(--white);font-size:12px;font-weight:300}
  .contact-row b{font-weight:600}

  /* back */
  .back-panel{position:absolute;inset:0}
  .keys-photo{position:absolute;left:255px;top:-19px;width:116px;height:116px;border-radius:50%;background:radial-gradient(circle at 60% 40%,#c7c0b4 0%,#9a8a74 45%,#6d5844 100%)}
  .back-headline{position:absolute;left:23px;top:27px;color:var(--yellow);font-family:"Fira Sans Condensed",sans-serif;font-size:15px;line-height:19px;font-weight:400}
  .back-headline b{color:var(--white);font-weight:600}

  .services{position:absolute;left:14px;top:88px;display:grid;grid-template-columns:103px 103px;row-gap:9px}
  .service{display:flex;flex-direction:column;align-items:center;color:var(--white);font-family:"Fira Sans Condensed",sans-serif;font-size:9.5px;line-height:11px}
  .service svg{width:18px;height:18px;margin-bottom:2px;fill:var(--white)}

  .back-contact{position:absolute;left:23px;color:var(--white);font-family:"Fira Sans Condensed",sans-serif;font-weight:400}
  .back-contact--web{top:278px;color:var(--yellow);font-size:12.5px}
  .back-contact--web b{font-weight:600}
  .back-contact--addr{top:302px;font-size:12.5px}

  .mail-box{position:absolute;border:1px dashed var(--pink);border-radius:8px;background:var(--white);display:flex;align-items:center;justify-content:center;color:var(--pink);font-size:12.5px}
  .mail-box--postage{left:360px;top:11px;width:100px;height:94px}
  .mail-box--address{left:251px;top:124px;width:209px;height:94px}

  .card--back .brand{left:268px;width:204px;top:282px;color:var(--navy)}
  .card--back .brand__name{font-size:20px;line-height:22px;letter-spacing:4px}
  .card--back .brand__sub{font-size:9.5px;line-height:12px;letter-spacing:2.6px}

  .side-label{position:absolute;top:606px;width:480px;text-align:center;color:var(--label);font-family:"Fira Sans Condensed",sans-serif;font-weight:600;font-size:34px}
  .side-label--front{left:108px}
  .side-label--back{left:614px}
</style>
</head>
<body>

<section class="card card--front">
  <div class="front-photo" role="img" aria-label="Photo of two business people giving a high five in an office, tinted blue"></div>
  <div class="front-copy">
    <h1 class="headline">CHOOSE THE RIGHT</h1>
    <p class="subhead">PROPERTY MANAGEMENT SYSTEM</p>
    <p class="tagline">Selecting the wrong manager could be your costliest mistake ever!</p>
  </div>
  <div class="brand">
    <span class="brand__name">BRIGHTKEY</span>
    <span class="brand__sub">PROPERTY MANAGEMENT</span>
  </div>
  <div class="contact-row">
    <span>Give us a call now: <b>(806) 555-0147</b></span>
    <span>Email us: <b>info@brightkeypm.com</b></span>
  </div>
</section>

<section class="card card--back">
  <svg class="back-panel" viewBox="0 0 480 339" aria-hidden="true"><polygon points="0,0 380,0 232,339 0,339" fill="var(--navy)"/></svg>
  <div class="keys-photo" role="img" aria-label="Photo of a small model house with house keys on a wooden table"></div>

  <p class="back-headline"><b>Maximize</b> your financial returns with<br>support from our rental specialists.</p>

  <div class="services">
    <div class="service"><svg viewBox="0 0 20 20"><path d="M10 2 1 10h3v8h5v-5h2v5h5v-8h3z"/></svg>Property Marketing</div>
    <div class="service"><svg viewBox="0 0 20 20"><circle cx="6.5" cy="6" r="3"/><circle cx="13.5" cy="6" r="3"/><path d="M1 16c0-3 2.5-5 5.5-5s5.5 2 5.5 5zM10 16c0-3 1.5-5 3.5-5 3 0 5.5 2 5.5 5z"/></svg>Tenant Screening</div>
    <div class="service"><svg viewBox="0 0 20 20"><text x="10" y="17" text-anchor="middle" font-size="19" font-weight="700" font-family="Fira Sans, sans-serif">$</text></svg>Rent Collection</div>
    <div class="service"><svg viewBox="0 0 20 20"><path d="M9 3l3-2 6 6-2 2-2-1-9 10-3-3 10-9-1-2z"/></svg>Maintenance</div>
    <div class="service"><svg viewBox="0 0 20 20"><path d="M8 1a7 7 0 1 0 4 12.7l4.6 4.6 2-2-4.6-4.6A7 7 0 0 0 8 1zm0 3a4 4 0 1 1 0 8 4 4 0 0 1 0-8z"/></svg>Property Inspections</div>
    <div class="service"><svg viewBox="0 0 20 20"><path d="M2 2h1.5v14H18v1.5H2z"/><rect x="6" y="9" width="2" height="5"/><rect x="9.5" y="5" width="2" height="9"/><rect x="13" y="7" width="2" height="7"/></svg>Financial Reporting</div>
    <div class="service"><svg viewBox="0 0 20 20"><path d="M10 1 3 4v5c0 4.5 3 8 7 10 4-2 7-5.5 7-10V4zm0 3v12.5C7.3 15 6 12.5 6 9.5V6z"/></svg>Evictions</div>
    <div class="service"><svg viewBox="0 0 20 20"><path d="M9.2 1h1.6v2.2l6 1.3v1.4l-.3.1 3 6.5c0 1.8-1.6 2.8-3.5 2.8s-3.5-1-3.5-2.8l3-6.4-4.7-1V17h4v2H5.2v-2h4V5.1l-4.7 1 3 6.4c0 1.8-1.6 2.8-3.5 2.8S.5 14.3.5 12.5l3-6.5-.3-.1V4.5l6-1.3zM4 8l-1.8 4h3.6zm12 0-1.8 4h3.6z"/></svg>Legal Guidance</div>
  </div>

  <p class="back-contact back-contact--web">Visit us at <b>www.brightkeyrentals-example.com</b></p>
  <p class="back-contact back-contact--addr">2287 Marble Lane, Lubbock, TX 79555</p>

  <div class="mail-box mail-box--postage">postage area</div>
  <div class="mail-box mail-box--address">address sticker label area</div>

  <div class="brand">
    <span class="brand__name">BRIGHTKEY</span>
    <span class="brand__sub">PROPERTY MANAGEMENT</span>
  </div>
</section>

<p class="side-label side-label--front">FRONT</p>
<p class="side-label side-label--back">BACK</p>

</body>
</html>
```